International Legal Service Company needs Letterhead Design

Put my new Logo into Letterhead Design, using updated telephone number, e-mail address and website. Current letterhead and updated information which i want you to include my new letterhead attached herewith. Of course, my new Logo attached herein. Also, you can use slogan "Total Legal Outsourcing Solutions For Multinational Businesses"

It Company

```html
<!DOCTYPE html>
<html lang="en">
<head>
<meta charset="utf-8">
<title>Meridian Counsel Group – Letterhead</title>
<link href="https://fonts.googleapis.com/css2?family=Fira+Sans:wght@400;500&family=Fira+Sans+Condensed:wght@700&family=Homemade+Apple&display=swap" rel="stylesheet">
<style>
  :root {
    --backdrop: #e6e6e4;
    --paper: #ffffff;
    --ink: #2b2b2b;
    --ink-soft: #3a3a3a;
    --brand-blue: #1f3f9a;
    --brand-mark: #2f56b8;
    --signature-blue: #5a6fb0;
  }
  * { margin: 0; padding: 0; box-sizing: border-box; }
  html, body {
    width: 1200px;
    height: 820px;
    overflow: hidden;
    background: var(--backdrop);
  }
  .letterhead {
    position: absolute;
    left: 330px;
    top: 30px;
    width: 540px;
    height: 760px;
    background: var(--paper);
    box-shadow: 0 2px 10px rgba(0,0,0,0.12);
    font-family: "Fira Sans", sans-serif;
    color: var(--ink);
  }
  .brand {
    position: absolute;
    top: 40px;
    left: 0;
    width: 100%;
    display: flex;
    justify-content: center;
    align-items: center;
    gap: 10px;
  }
  .brand-dot {
    width: 52px;
    height: 52px;
    border-radius: 50%;
    background: var(--brand-mark);
  }
  .brand-name {
    font-family: "Fira Sans", sans-serif;
    font-weight: 500;
    font-size: 19px;
    line-height: 1.15;
    color: var(--brand-blue);
  }
  .salutation {
    position: absolute;
    top: 178px;
    left: 45px;
    font-size: 20px;
    font-weight: 400;
  }
  .letter-body {
    position: absolute;
    top: 228px;
    left: 45px;
    right: 45px;
    font-size: 10.6px;
    line-height: 1.5;
    color: var(--ink-soft);
    text-align: justify;
  }
  .letter-body p { margin-bottom: 13px; }
  .closing {
    position: absolute;
    top: 530px;
    right: 45px;
    font-size: 10.6px;
    color: var(--ink-soft);
  }
  .signature {
    position: absolute;
    top: 562px;
    right: 45px;
    font-family: "Homemade Apple", cursive;
    font-size: 15px;
    color: var(--signature-blue);
  }
  .contact {
    position: absolute;
    top: 645px;
    left: 30px;
    font-family: "Fira Sans Condensed", sans-serif;
    font-weight: 700;
    font-size: 8.6px;
    line-height: 1.45;
    color: #111;
    font-style: normal;
  }
  .footer-mark {
    position: absolute;
    right: 58px;
    top: 660px;
    width: 58px;
    height: 58px;
    border-radius: 50%;
    background: var(--brand-mark);
    opacity: 0.55;
  }
</style>
</head>
<body>
  <main class="letterhead">
    <header class="brand">
      <span class="brand-dot" aria-hidden="true"></span>
      <span class="brand-name">Meridian Counsel<br>Group</span>
    </header>

    <h1 class="salutation">Dear Mr. Bennett,</h1>

    <section class="letter-body">
      <p>Lorem ipsum dolor sit amet, consectetur adipiscing elit. Donec orci purus, luctus vitae dignissim eu, iaculis sed purus. Vivamus faucibus, ipsum nec aliquet viverra, leo mauris condimentum ligula, sit amet sagittis enim ligula quis arcu. Nam egestas tortor id nisl porttitor mattis. In tortor ante, ultricies in suscipit a, tempus non massa. Vivamus et auctor mi. Fusce vel massa nulla. Phasellus nec eros mauris, et scelerisque orci.</p>
      <p>Donec malesuada orci vitae nulla accumsan porta a id massa. Quisque accumsan iaculis magna sit amet fringilla. Maecenas consequat, magna eget tincidunt semper, odio nibh rutrum mi, id feugiat ante nisi eu risus. Vestibulum nunc orci, rhoncus a placerat in, ultricies in mi. Cras mattis varius eros, vel fringilla nisl suscipit eget. Quisque scelerisque sagittis nulla at porttitor.</p>
      <p>Sed id augue vitae urna euismod commodo aliquet a quam. Pellentesque arcu velit, cursus et malesuada ut, consequat et diam. Nullam erat sem, rhoncus id ullamcorper vitae, rhoncus et arcu. In ultricies ultricies nulla, ut rutrum nisl iaculis at. Donec eu magna a metus ornare faucibus. Fusce aliquet faucibus ultricies. Morbi semper, est id tincidunt gravida, sem arcu adipiscing lacus, ac bibendum nulla leo eu purus. Quisque nec diam sed risus consectetur a ccumsan quis quis nibh. Vestibulum id purus lorem.</p>
    </section>

    <p class="closing">Sincerely,</p>
    <p class="signature">Alex Carter</p>

    <address class="contact">
      4180 Harbor Point Drive<br>
      Suite 210<br>
      Easton, MD 21601<br>
      Tel: 410-555-0137<br>
      Fax: 410-555-0184<br>
      E-Mail: office@meridiancounsel.example<br>
      Website: http://meridiancounsel.example
    </address>

    <span class="footer-mark" aria-hidden="true"></span>
  </main>
</body>
</html>
```